Business Card Design Project

We need a business card for a chiropractic and rehabilitation center. We already have a logo and need the card to follow the color and feel of the logo.

Target Market(s)

adults 30-55 that have some ache or pain that is interfering with their life, so much as they are ready to do something about it.

Industry/Entity Type

Business

```html
<!DOCTYPE html>
<html lang="en">
<head>
<meta charset="utf-8">
<title>Meridian Wellness Center – Business Card</title>
<link rel="stylesheet" href="https://fonts.googleapis.com/css2?family=Arimo:wght@400;700&display=swap">
<style>
  :root {
    --page: #e6e6e6;
    --slate: #58595b;
    --slate-dark: #4a4b4d;
    --crimson: #be1e2d;
    --amber: #f7941d;
    --paper: #ffffff;
    --ink: #3d3e40;
    --muted: #9a9a9a;
  }
  * { box-sizing: border-box; margin: 0; padding: 0; }
  html, body {
    width: 1067px; height: 1200px; overflow: hidden;
    background: var(--page);
    font-family: "Arimo", Arial, sans-serif;
  }
  .sheet {
    position: relative; width: 1067px; height: 1200px;
  }
  .card {
    position: absolute; left: 93px; width: 880px; height: 503px;
    overflow: hidden;
    box-shadow: 0 6px 18px rgba(0,0,0,.18);
  }
  .card--front { top: 50px; background: var(--slate); }
  .card--back { top: 640px; background: var(--paper); }
  .card__shapes { position: absolute; inset: 0; width: 100%; height: 100%; }

  /* front */
  .front__brand {
    position: absolute; left: 450px; top: 205px; width: 390px;
    color: var(--paper); font-weight: 700; font-size: 38px;
    letter-spacing: 1px; line-height: 1.1; text-align: center;
  }
  .front__web {
    position: absolute; left: 450px; top: 385px; width: 390px; text-align: center;
    color: var(--paper); font-size: 22px; letter-spacing: .3px;
  }

  /* back */
  .back__brand {
    position: absolute; left: 60px; top: 120px; width: 420px;
    color: var(--ink); font-weight: 700; font-size: 34px; letter-spacing: .5px; line-height: 1.1;
  }
  .back__rule {
    position: absolute; left: 60px; top: 210px; width: 130px; height: 2px; background: #cfcfcf;
  }
  .back__company { position: absolute; left: 60px; top: 260px; font-size: 19px; line-height: 1.45; color: var(--ink); }
  .back__person { position: absolute; right: 60px; top: 130px; text-align: right; font-size: 19px; line-height: 1.55; color: var(--ink); }
  .line { display: flex; align-items: center; gap: 10px; }
  .person .line, .back__person .line { justify-content: flex-end; }
  .web { color: var(--amber); }
  .name { color: var(--crimson); font-size: 22px; }
  .icon { width: 16px; height: 16px; flex: none; fill: var(--ink); }
  .icon--spacer { visibility: hidden; }
</style>
</head>
<body>
<main class="sheet">

  <section class="card card--front" aria-label="Card front">
    <svg class="card__shapes" viewBox="0 0 880 503" preserveAspectRatio="none" aria-hidden="true">
      <polygon points="270,0 545,0 220,503 0,503 0,377" fill="var(--crimson)"/>
      <polygon points="0,0 270,0 0,377" fill="var(--amber)"/>
    </svg>
    <p class="front__brand">MERIDIAN<br>WELLNESS CENTER</p>
    <p class="front__web">www.meridian-wellness.com</p>
  </section>

  <section class="card card--back" aria-label="Card back">
    <svg class="card__shapes" viewBox="0 0 880 503" preserveAspectRatio="none" aria-hidden="true">
      <polygon points="0,430 880,315 880,503 0,503" fill="var(--slate)"/>
      <polygon points="640,339 880,315 880,503 590,503" fill="var(--crimson)"/>
    </svg>

    <p class="back__brand">MERIDIAN<br>WELLNESS CENTER</p>
    <div class="back__rule"></div>

    <div class="back__company">
      <p class="line web">
        <svg class="icon" viewBox="0 0 16 16" aria-hidden="true"><circle cx="8" cy="8" r="7" fill="none" stroke="var(--ink)" stroke-width="1.5"/><path d="M1 8h14M8 1c-3 3-3 11 0 14M8 1c3 3 3 11 0 14" fill="none" stroke="var(--ink)" stroke-width="1.2"/></svg>
        www.meridian-wellness.com
      </p>
      <p class="line">
        <svg class="icon" viewBox="0 0 16 16" aria-hidden="true"><path d="M8 1 0 8h2v7h4v-5h4v5h4V8h2z"/></svg>
        2140 Meadow Ridge Dr, Ste 204
      </p>
      <p class="line">
        <svg class="icon icon--spacer" viewBox="0 0 16 16" aria-hidden="true"></svg>
        Austin TX 78745
      </p>
    </div>

    <div class="back__person">
      <p class="name">Dana Whitmore</p>
      <p class="line">dana@meridian-wellness.com
        <svg class="icon" viewBox="0 0 16 16" aria-hidden="true"><path d="M1 3h14v10H1z"/><path d="M1 3l7 6 7-6" fill="none" stroke="#fff" stroke-width="1.3"/></svg>
      </p>
      <p class="line">512.555.0148
        <svg class="icon" viewBox="0 0 16 16" aria-hidden="true"><path d="M3.6 1.2 6 4c.4.5.3 1.1-.1 1.5L4.7 6.6c.9 1.9 2.7 3.8 4.7 4.7l1.1-1.2c.4-.4 1-.5 1.5-.1l2.8 2.4c.4.4.4 1 0 1.4l-1.4 1.4C10.3 16 .1 5.7 1.1 2.6L2.2 1.2c.4-.4 1-.4 1.4 0z"/></svg>
      </p>
    </div>
  </section>

</main>
</body>
</html>
```